Rotomould Brochure

We need a conference brochure designed with a copy ready for print and also a PDF copy for email usage. We have mocked up something in word with the wording, the specific ads and images are provided in the file crate folder.

https://www.filecrate.net/sh/qk4tr82mxp51c07/HvLnQbsWERk?n=57104362

Reason: I have extended the deadline and offered more money as we understand the work is required.

```html
<!DOCTYPE html>
<html lang="en">
<head>
<meta charset="UTF-8">
<title>Rotocraft 2014 – Conference &amp; Trade Exhibition</title>
<link rel="stylesheet" href="https://fonts.googleapis.com/css2?family=Open+Sans:ital,wght@0,400;0,600;1,400;1,600&display=swap">
<style>
  :root {
    --paper: #eeeeef;
    --edge: #9a9a9a;
    --navy: #18386a;
    --lime: #8cc63e;
    --lime-band: #d5f03a;
    --sky-band: #1b8fd9;
    --ink: #2a2a2a;
    --divider: #ffffff;
  }
  * { margin: 0; padding: 0; box-sizing: border-box; }
  html, body { width: 849px; height: 1200px; overflow: hidden; background: var(--paper); }
  .brochure-cover {
    position: relative;
    width: 849px;
    height: 1200px;
    background: var(--paper);
    border: 1px solid var(--edge);
    font-family: "Open Sans", Arial, sans-serif;
    overflow: hidden;
  }
  .event-header {
    position: absolute;
    left: 60px;
    top: 116px;
  }
  .event-title {
    font-size: 46px;
    font-weight: 400;
    color: var(--navy);
    line-height: 1;
    letter-spacing: 0.2px;
  }
  .event-subtitle {
    margin-top: 6px;
    font-size: 18.5px;
    font-weight: 400;
    color: var(--lime);
    line-height: 1.1;
  }
  .event-venue {
    margin-top: 1px;
    font-size: 17px;
    font-style: italic;
    color: var(--ink);
    line-height: 1.2;
  }
  .event-dates {
    font-size: 20px;
    font-style: italic;
    font-weight: 600;
    color: var(--navy);
    line-height: 1.15;
  }
  .band-graphic {
    position: absolute;
    left: 0;
    top: 250px;
    width: 849px;
    height: 700px;
  }
  .roadshow-footer {
    position: absolute;
    right: 62px;
    top: 955px;
    text-align: right;
  }
  .roadshow-title {
    font-size: 30px;
    font-weight: 400;
    color: var(--navy);
    line-height: 1.1;
  }
  .roadshow-location {
    margin-top: 2px;
    font-size: 16px;
    font-style: italic;
    color: var(--ink);
    line-height: 1.3;
  }
  .roadshow-date {
    font-size: 20px;
    font-style: italic;
    font-weight: 600;
    color: var(--navy);
    line-height: 1.1;
  }
</style>
</head>
<body>
  <main class="brochure-cover">
    <header class="event-header">
      <h1 class="event-title">ROTOCRAFT 2014</h1>
      <p class="event-subtitle">CONFERENCE &amp; TRADE EXHIBITION</p>
      <p class="event-venue">Harbourview Grand Coogee Beach, Sydney</p>
      <p class="event-dates">22 - 24 June</p>
    </header>

    <svg class="band-graphic" viewBox="0 0 849 700" xmlns="http://www.w3.org/2000/svg">
      <defs>
        <linearGradient id="sydney-night" x1="0" y1="0" x2="0" y2="1">
          <stop offset="0" stop-color="#0b1a3a"/>
          <stop offset="0.45" stop-color="#1d5fb0"/>
          <stop offset="0.62" stop-color="#6a5a48"/>
          <stop offset="0.8" stop-color="#1c3f8c"/>
          <stop offset="1" stop-color="#0d1d48"/>
        </linearGradient>
        <linearGradient id="auckland-dusk" x1="0" y1="0" x2="0" y2="1">
          <stop offset="0" stop-color="#5a4636"/>
          <stop offset="0.35" stop-color="#e0a24a"/>
          <stop offset="0.55" stop-color="#c98a3e"/>
          <stop offset="0.72" stop-color="#2b2a30"/>
          <stop offset="1" stop-color="#14161c"/>
        </linearGradient>
      </defs>

      <polygon class="lime-pointer" points="91,49 135,4 177,49" fill="var(--lime-band)"/>
      <rect class="lime-band" x="0" y="49" width="849" height="22" fill="var(--lime-band)"/>

      <g role="img" aria-label="Photo of the Sydney harbour opera house lit with colourful projections at night">
        <polygon points="0,71 656,71 396,617 0,617" fill="url(#sydney-night)"/>
      </g>
      <g role="img" aria-label="Photo of the Auckland skyline and its tower at sunset">
        <polygon points="664,71 849,71 849,617 404,617" fill="url(#auckland-dusk)"/>
      </g>
      <polygon class="photo-divider" points="656,71 664,71 404,617 396,617" fill="var(--divider)"/>

      <rect class="sky-band" x="0" y="617" width="849" height="25" fill="var(--sky-band)"/>
      <polygon class="sky-pointer" points="678,642 758,642 718,694" fill="var(--sky-band)"/>
    </svg>

    <footer class="roadshow-footer">
      <h2 class="roadshow-title">ROTOCRAFT ON THE ROAD</h2>
      <p class="roadshow-location">Auckland, New Zealand</p>
      <p class="roadshow-date">June 26th</p>
    </footer>
  </main>
</body>
</html>
```